Scripture-Rooted Covenant Church of Willow Crossing 2024 Theme

We, Scripture-Rooted Covenant Church of Willow Crossing, need a design for two banners; (1) a Horizontal 6' x 4' banner that will be placed on one wall in the main sanctuary, (2) a retractable banner. The banners are to communicate/advertise the church's theme for 2024, "Endeavoring to Grow, Know and Love God More in 2024" (2 Timothy 2:15). The design should include our logo and church name. Use the color purple. This banner should be reflective of growth, knowledge, love of God. Our congregation demographic is 98% African American, 2% Hispanic. Our home base is Tampa, Florida (USA), but we have a small social media following.

Target Market(s)

Church members and visitors; male and female ages 1-99

Industry/Entity Type

Religious

Colors
6B429C
8869AF
B7A5CE
E3DAEB
F3F0F8

Requirements
Must have
• Church logo, color purple
Nice to have
• Vibrant design; colors that complement purple

```html
<!DOCTYPE html>
<html lang="en">
<head>
<meta charset="UTF-8">
<title>Scripture-Rooted Covenant Church of Willow Crossing – 2024 Theme Banners</title>
<link href="https://fonts.googleapis.com/css2?family=Cinzel:wght@600;700&family=Kaushan+Script&display=swap" rel="stylesheet">
<style>
  :root {
    --page-bg: #aaaaaa;
    --purple-deep: #2a0f4a;
    --purple: #4a1f7a;
    --purple-mid: #5a2a8c;
    --lilac: #b7a5ce;
    --silver: #d9d9de;
    --silver-dark: #8e8e96;
    --white: #ffffff;
    --sky-top: #2d2a5e;
    --sky-mid: #8a6f96;
    --sky-glow: #f3c9a0;
    --hill: #140d18;
    --ink: #0b0b0d;
  }
  * { margin: 0; padding: 0; box-sizing: border-box; }
  html, body { width: 1200px; height: 1200px; overflow: hidden; background: var(--page-bg); }
  .canvas { position: relative; width: 1200px; height: 1200px; }

  .banner {
    position: absolute;
    overflow: hidden;
    background: radial-gradient(ellipse at 50% 55%, var(--purple-mid), var(--purple) 55%, var(--purple-deep));
    font-family: "Cinzel", serif;
    color: var(--white);
  }
  .banner--retractable { left: 72px; top: 112px; width: 416px; height: 975px; }
  .banner--wall { left: 538px; top: 395px; width: 616px; height: 410px; }

  .sky-photo {
    position: absolute; left: 0; top: 0; width: 100%;
    background:
      radial-gradient(ellipse at 52% 55%, var(--sky-glow) 0%, #d99a86 25%, transparent 60%),
      linear-gradient(180deg, var(--sky-top) 0%, var(--sky-mid) 45%, #e7a889 80%, var(--hill) 100%);
  }
  .banner--retractable .sky-photo { height: 372px; clip-path: polygon(0 0,100% 0,100% 100%,50% 85%,0 100%); }
  .banner--wall .sky-photo { height: 201px; clip-path: polygon(0 0,100% 0,100% 100%,50% 58%,0 100%); }

  .roof-line { position: absolute; left: 0; top: 0; width: 100%; height: 100%; pointer-events: none; }

  .church-mark { position: absolute; left: 0; width: 100%; text-align: center; }
  .church-mark__seal { display: block; margin: 0 auto; border-radius: 50%; background: var(--lilac); }
  .church-mark__name { font-weight: 700; color: var(--white); line-height: 1.15; letter-spacing: .02em; }

  .theme__lead { position: absolute; left: 0; width: 100%; text-align: center; font-weight: 700; letter-spacing: .01em; line-height: 1; }
  .theme__verbs {
    position: absolute; border: 3px solid var(--silver-dark); outline: 2px solid var(--silver); outline-offset: -7px;
    display: flex; align-items: center; justify-content: center; font-weight: 700;
    text-shadow: 0 0 8px rgba(255,255,255,.9);
  }
  .theme__god {
    position: absolute; left: 0; width: 100%; text-align: center;
    font-family: "Kaushan Script", cursive; line-height: 1;
    background: linear-gradient(170deg, #ffffff 20%, #9c9ca6 45%, #ffffff 60%, #b8b8c0 85%);
    -webkit-background-clip: text; background-clip: text; color: transparent;
    filter: drop-shadow(0 0 6px rgba(255,255,255,.5));
  }
  .theme__more { position: absolute; left: 0; width: 100%; display: flex; justify-content: center; align-items: center; font-weight: 700; color: #e6e0ee; line-height: 1; }
  .theme__more::before, .theme__more::after { content: ""; background: var(--silver); height: 2px; }
  .theme__year { position: absolute; left: 0; width: 100%; text-align: center; font-weight: 700; line-height: 1; }
  .theme__rule { position: absolute; height: 2px; background: linear-gradient(90deg, transparent, var(--white), transparent); }
  .theme__verse { position: absolute; left: 0; width: 100%; text-align: center; font-weight: 700; font-variant: small-caps; line-height: 1; }

  .corner { position: absolute; left: 0; top: 0; }

  /* retractable sizing */
  .banner--retractable .church-mark { top: 236px; }
  .banner--retractable .church-mark__seal { width: 54px; height: 54px; }
  .banner--retractable .church-mark__name { font-size: 10px; margin-top: 5px; }
  .banner--retractable .theme__lead { top: 414px; font-size: 27px; }
  .banner--retractable .theme__verbs { left: 18px; top: 459px; width: 379px; height: 59px; font-size: 30px; }
  .banner--retractable .theme__god { top: 500px; font-size: 170px; }
  .banner--retractable .theme__more { top: 696px; font-size: 28px; gap: 12px; }
  .banner--retractable .theme__more::before, .banner--retractable .theme__more::after { width: 30px; }
  .banner--retractable .theme__year { top: 736px; font-size: 76px; }
  .banner--retractable .theme__rule { left: 88px; width: 240px; top: 820px; }
  .banner--retractable .theme__verse { top: 850px; font-size: 26px; }

  /* wall sizing */
  .banner--wall .church-mark { top: 56px; }
  .banner--wall .church-mark__seal { width: 30px; height: 30px; }
  .banner--wall .church-mark__name { font-size: 7px; margin-top: 3px; }
  .banner--wall .theme__lead { top: 150px; font-size: 17px; }
  .banner--wall .theme__verbs { left: 162px; top: 170px; width: 291px; height: 43px; font-size: 21px; }
  .banner--wall .theme__god { top: 203px; font-size: 88px; }
  .banner--wall .theme__more { top: 301px; font-size: 15px; gap: 10px; }
  .banner--wall .theme__more::before, .banner--wall .theme__more::after { width: 46px; }
  .banner--wall .theme__year { top: 318px; font-size: 40px; }
  .banner--wall .theme__rule { left: 168px; width: 280px; top: 362px; }
  .banner--wall .theme__verse { top: 370px; font-size: 15px; }
  .banner--wall .ground-strip { position: absolute; left: 0; bottom: 0; width: 100%; height: 19px; background: var(--ink); }
</style>
</head>
<body>
<main class="canvas">

  <section class="banner banner--retractable" aria-label="Retractable banner">
    <div class="sky-photo" role="img" aria-label="Sunrise sky with light rays and clouds behind a wooden cross on a hill, wrapped by a silver ribbon"></div>
    <svg class="roof-line" viewBox="0 0 416 975" aria-hidden="true">
      <polyline points="0,372 208,316 416,372" fill="none" stroke="#d9d9de" stroke-width="5"/>
    </svg>
    <div class="church-mark">
      <span class="church-mark__seal"></span>
      <p class="church-mark__name">Scripture-Rooted Covenant Church<br>of Willow Crossing</p>
    </div>
    <p class="theme__lead">ENDEAVORING TO</p>
    <div class="theme__verbs">GROW, KNOW, LOVE,</div>
    <p class="theme__god">God</p>
    <p class="theme__more">MORE IN</p>
    <p class="theme__year">2024</p>
    <div class="theme__rule"></div>
    <p class="theme__verse">2 Timothy 2:15</p>
    <svg class="corner" width="416" height="975" viewBox="0 0 416 975" aria-hidden="true" fill="none" stroke="#d9d9de" stroke-width="5">
      <polyline points="20,750 20,940 190,940"/>
      <polyline points="35,762 35,955 175,955"/>
      <polyline points="396,750 396,940 226,940"/>
      <polyline points="381,762 381,955 241,955"/>
    </svg>
  </section>

  <section class="banner banner--wall" aria-label="Horizontal wall banner">
    <div class="sky-photo" role="img" aria-label="Wide sunrise sky with clouds and dark hills, a wooden cross wrapped by a silver ribbon"></div>
    <svg class="roof-line" viewBox="0 0 616 410" aria-hidden="true">
      <polyline points="0,201 308,117 616,201" fill="none" stroke="#d9d9de" stroke-width="4"/>
    </svg>
    <div class="church-mark">
      <span class="church-mark__seal"></span>
      <p class="church-mark__name">Scripture-Rooted Covenant Church<br>of Willow Crossing</p>
    </div>
    <p class="theme__lead">ENDEAVORING TO</p>
    <div class="theme__verbs">GROW, KNOW, LOVE,</div>
    <p class="theme__god">God</p>
    <p class="theme__more">MORE IN</p>
    <p class="theme__year">2024</p>
    <div class="theme__rule"></div>
    <p class="theme__verse">2 Timothy 2:15</p>
    <svg class="corner" width="616" height="410" viewBox="0 0 616 410" aria-hidden="true" fill="none" stroke="#d9d9de" stroke-width="3">
      <polyline points="19,254 19,385 122,385"/>
      <polyline points="29,262 29,393 112,393"/>
      <polyline points="597,254 597,385 494,385"/>
      <polyline points="587,262 587,393 504,393"/>
    </svg>
    <div class="ground-strip"></div>
  </section>

</main>
</body>
</html>
```